Telecommunications/Power civil contractor needs business card design

Were a new telecommunications/power underground civil contractor that is looking for a new business card design. Our company colours are silver or grey and orange. Feel free to use the white background logo or the black background logo.

Target Market(s)

Local contractors, utility companies, private sector mining/energy companies, developers.

Industry/Entity Type

Telecommunications

Contact Information for Business Card

Each card will need the following info:
Persons name:
Title:
E-mail:
Phone number:
Shop Address:
Mailing Address:

Requirements
Must have
• Each card will need the following info:
• Persons name:
• Title:
• E-mail:
• Phone number:
• Shop Address:
• Mailing Address:

```html
<!DOCTYPE html>
<html lang="en">
<head>
<meta charset="utf-8">
<title>Delta Line Contracting Inc – Business Card</title>
<link href="https://fonts.googleapis.com/css2?family=Open+Sans:wght@400;700&display=swap" rel="stylesheet">
<style>
  :root {
    --stage: #3d2c36;
    --card-dark: #231f20;
    --card-light: #ffffff;
    --brand-orange: #f05a28;
    --brand-grey: #636466;
    --text-light: #ffffff;
  }
  * { margin: 0; padding: 0; box-sizing: border-box; }
  html, body { width: 1200px; height: 1200px; overflow: hidden; }
  body {
    background: var(--stage);
    font-family: "Open Sans", Arial, sans-serif;
    position: relative;
  }
  .card {
    position: absolute;
    left: 202px;
    width: 796px;
    height: 450px;
    box-shadow: 0 6px 14px rgba(0,0,0,0.45);
    overflow: hidden;
  }
  .card--front { top: 110px; background: var(--card-dark); }
  .card--back { top: 640px; background: var(--card-light); }

  .brand-mark {
    position: absolute;
    width: 152px;
    height: 152px;
    border: 5px solid var(--brand-grey);
    border-radius: 50%;
  }
  .card--front .brand-mark { left: 322px; top: 102px; }
  .card--back .brand-mark { left: 128px; top: 94px; }

  .brand-name {
    position: absolute;
    text-align: center;
    color: var(--brand-orange);
    font-weight: 700;
    line-height: 1;
  }
  .brand-name__main { display: block; font-size: 46px; letter-spacing: 3px; }
  .brand-name__sub { display: block; font-size: 19px; letter-spacing: 2.5px; margin-top: 8px; }
  .card--front .brand-name { left: 0; width: 796px; top: 286px; }
  .card--back .brand-name { left: 34px; width: 340px; top: 276px; }

  .front-url {
    position: absolute;
    left: 0; width: 796px; top: 416px;
    text-align: center;
    color: var(--text-light);
    font-size: 19px;
  }

  .contact-panel {
    position: absolute;
    left: 415px; top: 0;
    width: 381px; height: 450px;
    background: var(--brand-orange);
  }
  .accent-band {
    position: absolute;
    left: 392px; top: 42px;
    width: 46px; height: 368px;
    background: var(--brand-grey);
  }
  .accent-fold { position: absolute; left: 392px; top: 410px; }

  .person-name {
    position: absolute; left: 460px; top: 36px;
    color: var(--text-light); font-size: 29px;
  }
  .person-title {
    position: absolute; left: 461px; top: 74px;
    color: var(--text-light); font-size: 20px;
  }
  .contact-list { position: absolute; left: 462px; top: 134px; list-style: none; color: var(--text-light); font-size: 20px; }
  .contact-list li { display: flex; align-items: center; height: 26.5px; }
  .contact-list svg { width: 16px; height: 16px; margin-right: 14px; flex: none; }

  .address {
    position: absolute; left: 462px;
    display: flex; align-items: flex-start;
    color: var(--text-light); font-size: 20px; line-height: 26.5px;
  }
  .address svg { width: 16px; height: 20px; margin: 4px 14px 0 0; flex: none; }
  .address--shop { top: 236px; }
  .address--mail { top: 338px; }
</style>
</head>
<body>

<section class="card card--front">
  <div class="brand-mark"></div>
  <div class="brand-name">
    <span class="brand-name__main">DELTA LINE</span>
    <span class="brand-name__sub">CONTRACTING INC</span>
  </div>
  <p class="front-url">www.deltalineinc.com</p>
</section>

<section class="card card--back">
  <div class="brand-mark"></div>
  <div class="brand-name">
    <span class="brand-name__main">DELTA LINE</span>
    <span class="brand-name__sub">CONTRACTING INC</span>
  </div>

  <div class="contact-panel"></div>
  <div class="accent-band"></div>
  <svg class="accent-fold" width="46" height="24" viewBox="0 0 46 24"><polygon points="0,0 46,0 24,24" fill="#8a8b8d"/></svg>

  <h1 class="person-name">Marcus Hale</h1>
  <p class="person-title">Managing Partner</p>

  <ul class="contact-list">
    <li>
      <svg viewBox="0 0 16 16"><path d="M1 6c0-2 3-3 7-3s7 1 7 3v1h-3V5.5C11 5 10 5 8 5s-3 0-4 .5V7H1z M4 8h8l2 6H2z" fill="#fff"/></svg>
      000.000.0000
    </li>
    <li>
      <svg viewBox="0 0 16 16"><rect x="1" y="3.5" width="14" height="9" fill="#fff"/><path d="M1 3.5l7 5 7-5" stroke="#f05a28" stroke-width="1.2" fill="none"/></svg>
      marcus@deltalineinc.com
    </li>
    <li>
      <svg viewBox="0 0 16 16" fill="none" stroke="#fff" stroke-width="1.2"><circle cx="8" cy="8" r="6.5"/><ellipse cx="8" cy="8" rx="3" ry="6.5"/><path d="M1.5 8h13M2.5 5h11M2.5 11h11"/></svg>
      www.deltalineinc.com
    </li>
  </ul>

  <div class="address address--shop">
    <svg viewBox="0 0 16 20"><path d="M8 1a6 6 0 0 1 6 6c0 4.5-6 12-6 12S2 11.5 2 7a6 6 0 0 1 6-6z" fill="#fff"/><circle cx="8" cy="7" r="2.3" fill="#f05a28"/></svg>
    <p>Shop Address:<br>3175 Alder Avenue<br>Riverton, TN 38141</p>
  </div>
  <div class="address address--mail">
    <svg viewBox="0 0 16 20"><path d="M8 1a6 6 0 0 1 6 6c0 4.5-6 12-6 12S2 11.5 2 7a6 6 0 0 1 6-6z" fill="#fff"/><circle cx="8" cy="7" r="2.3" fill="#f05a28"/></svg>
    <p>Mailing Address:<br>5206 Harlow Road<br>Eastbrook, NY 10614</p>
  </div>
</section>

</body>
</html>
```